LOLU Baby Massage Classes - flyer to make a difference

I need a single page flyer, preferably single page, to hand out to doctors, medical centres and parents. To also leave on counters of establishments.
It is to promote my baby massage classes. Mums can get together with other mums and book a 5 week course to learn and discover the many benefits of baby massage.
Benefits include: enhances bonding and attachment, understand non-verbal cues from your baby, helps with sleep patterns, help with immune system, increases vagal activity,relief from wind, colic or constipation to name some.

Baby age from birth to 12 months. Group classes or private sessions

I am a Professional Member and Certified by the Global Society of Newborn Touch (GSNT) GSNT Australia is Nationally Accredited and is endorsed by Crown Academy of Carers, the Southern Guild of Birth Attendants, The Southern Union of Daily Living Therapy Australia, The Southern Union of Bodywork Practitioner and is a full member of Wellmind Network Australia.

Class detail and availability contact is Petra Holm 0487 315 208 petra.joanne.holm@quillmail.example www.lolunewborntouch com.au facebook/comLOLUnewborntouch

My colour scheme is green and purple as you will see from my logo and website. I would like my flyer to be softer tones of either both colours or just one.

I will include some images you can choose from or show me any you think will fit in with baby massage. THANK YOU
Updates

Hi The size of my flyer is A6. Approx 150mms x 210mms and single sided. Thank you

Target Market(s)

mums and dads, groups, doctors, midwives

Industry/Entity Type

Medical

Font styles to use
Sans Serif

Colors
87d0c7
b09cc8

Requirements
Must have
• baby photo or photos, both my logo and the GSNT logo. The GSNT logo is to be small
• Baby Massage Classes (wording) is very important to catch the eye.
• Invitation to book a class or gather friends to book is next in importance
• Benefits is next
• The admin information ie.,membership, certification and endorsements are lesser and can be small.
• Contact information to be noticeable.
Nice to have
• If you have an idea, drawing or photo that would look better, please feel free to try it
Should not have
• should not be crowded with information all the same size

```html
<!DOCTYPE html>
<html lang="en">
<head>
<meta charset="utf-8">
<title>LOLU Baby Massage Classes</title>
<link rel="stylesheet" href="https://fonts.googleapis.com/css2?family=Fredoka:wght@500;600;700&family=Open+Sans:wght@400;600;700;800&display=swap">
<style>
  :root {
    --purple: #7a3e8e;
    --purple-deep: #5f2a73;
    --magenta: #a2388f;
    --green: #8cc63f;
    --green-soft: #87d0c7;
    --lilac: #b09cc8;
    --lilac-pale: #efe8f4;
    --ink: #3a3a3a;
    --white: #ffffff;
  }
  * { margin: 0; padding: 0; box-sizing: border-box; }
  html, body { width: 859px; height: 1200px; overflow: hidden; background: var(--white); }
  .flyer {
    position: relative; width: 859px; height: 1200px; overflow: hidden;
    background: var(--white); font-family: "Open Sans", Arial, sans-serif; color: var(--ink);
  }
  .baby-photo {
    position: absolute; left: 390px; top: 160px; width: 469px; height: 800px;
    background: radial-gradient(ellipse at 45% 40%, #f6e1d6 0%, #ecc9b8 45%, #d9b7a8 75%, #c9b2b6 100%);
  }
  .title-baby { position: absolute; left: 90px; top: 40px; display: flex; gap: 8px; }
  .title-baby span {
    width: 112px; height: 112px; border-radius: 50%;
    border: 5px solid var(--purple); background: var(--white);
    display: flex; align-items: center; justify-content: center;
    font-family: "Fredoka", sans-serif; font-weight: 700; font-size: 84px; color: var(--magenta);
    line-height: 1;
  }
  .title-baby span:nth-child(2) { margin-top: 18px; }
  .title-baby span:nth-child(4) { margin-top: 12px; }
  .title-massage { position: absolute; left: 50px; top: 150px; width: 560px; height: 100px; }
  .partner-mark {
    position: absolute; left: 640px; top: 60px; display: flex; align-items: center; gap: 14px;
  }
  .partner-mark .dot { width: 44px; height: 44px; border-radius: 50%; background: var(--purple); }
  .partner-mark .name { font-family: "Open Sans", sans-serif; font-weight: 700; font-size: 50px; color: var(--purple); }
  .intro {
    position: absolute; left: 34px; top: 262px; width: 380px;
    font-size: 19px; line-height: 1.28; font-weight: 600; color: var(--ink);
  }
  .benefits-label {
    position: absolute; left: 34px; top: 386px; padding: 3px 16px;
    background: var(--green); color: var(--white); font-weight: 800; font-size: 21px;
    border-radius: 0 14px 14px 0;
  }
  .benefits {
    position: absolute; left: 34px; top: 424px; width: 370px;
    font-size: 18px; line-height: 1.28; color: var(--ink);
  }
  .age-note {
    position: absolute; left: 34px; top: 580px; width: 360px;
    font-size: 21px; line-height: 1.25; font-weight: 700; color: var(--purple);
  }
  .credentials {
    position: absolute; left: 34px; top: 660px; width: 360px;
    font-size: 16px; line-height: 1.3; color: var(--ink);
  }
  .footer-wave { position: absolute; left: 0; top: 900px; width: 859px; height: 300px; }
  .client-mark {
    position: absolute; left: 40px; top: 1040px; display: flex; align-items: center; gap: 14px;
  }
  .client-mark .dot { width: 54px; height: 54px; border-radius: 50%; background: var(--green); }
  .client-mark .name { font-weight: 800; font-size: 46px; color: var(--green); }
  .client-tag {
    position: absolute; left: 40px; top: 1104px; width: 300px;
    font-size: 17px; font-weight: 700; color: var(--green); line-height: 1.2;
  }
  .contact {
    position: absolute; left: 430px; top: 1000px; width: 420px;
    color: var(--white); font-size: 20px; line-height: 1.3; font-weight: 600;
  }
  .contact .heading { color: #cfe8a6; font-size: 24px; font-weight: 700; }
</style>
</head>
<body>
<div class="flyer">
  <div class="baby-photo" role="img" aria-label="Photo of a smiling baby lying down receiving a tummy massage from a parent's hands"></div>

  <div class="title-baby" aria-label="Baby"><span>B</span><span>A</span><span>B</span><span>Y</span></div>

  <svg class="title-massage" viewBox="0 0 560 100" aria-label="Massage">
    <path d="M10 38 Q280 0 550 30 L545 92 Q280 70 15 96 Z" fill="var(--green)"/>
    <text x="280" y="74" text-anchor="middle" font-family="Fredoka, sans-serif" font-weight="700" font-size="58" fill="#ffffff" letter-spacing="4">MASSAGE</text>
  </svg>

  <div class="partner-mark"><span class="dot"></span><span class="name">GSNT</span></div>

  <p class="intro">Mums can get together with other mums and book a 5 week course to learn and discover the many benefits of baby massage.</p>

  <div class="benefits-label">Benefits include</div>
  <p class="benefits">Enhances bonding and attachment, understand non-verbal cues from your baby, helps with sleep patterns, help with immune system, increases vagal activity,relief from wind, colic or constipation to name some.</p>

  <p class="age-note">Baby age from birth to 12 months. Group classes or private sessions</p>

  <p class="credentials">I am a Professional Member and Certified by the Global Society of Newborn Touch (GSNT) GSNT Australia is Nationally Accredited and is endorsed by Crown Academy of Carers, the Southern Guild of Birth Attendants, The Southern Union of Daily Living Therapy Australia, The Southern Union of Bodywork Practitioner and is a full member of Wellmind Network Australia.</p>

  <svg class="footer-wave" viewBox="0 0 859 300" preserveAspectRatio="none" aria-hidden="true">
    <path d="M0 70 Q200 20 420 60 Q640 100 859 40 L859 300 L0 300 Z" fill="var(--lilac)"/>
    <path d="M0 95 Q220 45 430 82 Q650 120 859 62 L859 300 L0 300 Z" fill="var(--lilac-pale)"/>
    <path d="M400 80 Q640 118 859 60 L859 300 L400 300 Z" fill="var(--purple)"/>
    <path d="M400 80 Q380 190 400 300" fill="none" stroke="var(--purple)" stroke-width="0"/>
  </svg>

  <div class="client-mark"><span class="dot"></span><span class="name">lolu</span></div>
  <p class="client-tag">newborn touch instruction</p>

  <div class="contact">
    <p class="heading">Class detail and availability</p>
    <p>contact is Petra Holm 0487 315 208</p>
    <p>petra.joanne.holm@quillmail.example</p>
    <p>www.lolunewborntouch com.au</p>
    <p>facebook/comLOLUnewborntouch</p>
  </div>
</div>
</body>
</html>
```